VMR business card

Need a business card for a company that provides instructional design and elearning development services. The website is here: http://vantmoro.studio/

I'm attaching a current logo, as well as the old business card design. While I like to keep it clean, the old design is too simplistic for my liking. The only idea I want to reuse from the old design is placing industry jargon on the back of the card, just need a better way to present it. But if you have other ideas for the back--feel free to experiment.

Please use the colors complementary to the color we have on the website. Thank you!

```html
<!DOCTYPE html>
<html lang="en">
<head>
<meta charset="utf-8">
<title>VMR business card</title>
<link rel="stylesheet" href="https://fonts.googleapis.com/css2?family=Montserrat:wght@600;800&family=Open+Sans:wght@300;400&display=swap">
<style>
  :root {
    --page: #f4f4f4;
    --card-white: #f7f7f5;
    --ink: #3a3a3a;
    --ink-soft: #5a5a5a;
    --teal: #14a99a;
    --lime: #a8c66a;
    --sand: #e6d487;
    --orange: #f6a83f;
    --jargon: #2f2a24;
    --white: #ffffff;
  }
  * { box-sizing: border-box; margin: 0; padding: 0; }
  html, body { width: 1200px; height: 873px; overflow: hidden; }
  body {
    background: var(--page);
    display: flex;
    align-items: center;
    justify-content: center;
    gap: 60px;
  }
  .card {
    width: 500px;
    height: 286px;
    position: relative;
    overflow: hidden;
    box-shadow: 0 12px 30px rgba(0,0,0,0.12);
  }

  /* Front */
  .card-front {
    background: var(--card-white);
    font-family: "Open Sans", sans-serif;
    color: var(--ink);
  }
  .brand {
    position: absolute;
    top: 36px;
    left: 44px;
    display: flex;
    align-items: center;
    gap: 10px;
  }
  .brand-square {
    width: 14px;
    height: 14px;
    background: var(--teal);
  }
  .brand-name {
    font-size: 26px;
    font-weight: 400;
    color: var(--teal);
    letter-spacing: 0.5px;
  }
  .contact {
    position: absolute;
    left: 44px;
    top: 112px;
    list-style: none;
    font-weight: 300;
    font-size: 15px;
  }
  .contact-name {
    font-size: 17px;
    margin-bottom: 10px;
    color: var(--ink);
  }
  .contact li {
    display: flex;
    align-items: center;
    gap: 12px;
    height: 24px;
    color: var(--ink-soft);
  }
  .contact svg { width: 13px; height: 13px; flex: none; }
  .band {
    position: absolute;
    left: 0; right: 0; bottom: 0;
    height: 14px;
    background: linear-gradient(90deg, var(--teal), var(--lime) 65%, var(--sand));
  }

  /* Back */
  .card-back {
    background: var(--orange);
    font-family: "Montserrat", sans-serif;
    color: var(--jargon);
    padding: 30px 36px;
    display: flex;
    flex-direction: column;
    justify-content: space-between;
  }
  .services-label {
    font-weight: 600;
    font-size: 12px;
    letter-spacing: 3px;
    color: var(--white);
  }
  .services {
    list-style: none;
    font-weight: 800;
    font-size: 19px;
    line-height: 30px;
    letter-spacing: 0.3px;
  }
  .services li { white-space: nowrap; }
  .services .dot { color: var(--white); padding: 0 6px; }
  .closing {
    font-weight: 800;
    font-size: 24px;
    color: var(--white);
    border-top: 2px solid var(--jargon);
    padding-top: 12px;
    white-space: nowrap;
  }
</style>
</head>
<body>
  <section class="card card-front">
    <div class="brand">
      <span class="brand-square"></span>
      <span class="brand-name">Vantmoro Studio</span>
    </div>
    <ul class="contact">
      <li class="contact-name">Dorian Kessler</li>
      <li>
        <svg viewBox="0 0 16 16"><path fill="var(--teal)" d="M3 1h3l1.5 4-2 1.2a9 9 0 0 0 4.3 4.3L11 8.5l4 1.5v3c0 1-1 2-2 2A13 13 0 0 1 1 3c0-1 1-2 2-2z"/></svg>
        555-014-2287
      </li>
      <li>
        <svg viewBox="0 0 16 16"><rect x="1" y="3" width="14" height="10" rx="1.5" fill="var(--teal)"/><path d="M1.5 4l6.5 5 6.5-5" fill="none" stroke="var(--card-white)" stroke-width="1.4"/></svg>
        dkessler@vantmoro.studio
      </li>
      <li>
        <svg viewBox="0 0 16 16"><circle cx="8" cy="8" r="6.5" fill="none" stroke="var(--teal)" stroke-width="1.6"/><path d="M1.5 8h13M8 1.5c-3 3.5-3 9.5 0 13M8 1.5c3 3.5 3 9.5 0 13" fill="none" stroke="var(--teal)" stroke-width="1.2"/></svg>
        www.vantmoro.studio
      </li>
    </ul>
    <div class="band"></div>
  </section>

  <section class="card card-back">
    <p class="services-label">WHAT WE BUILD</p>
    <ul class="services">
      <li>STORYBOARDS<span class="dot">·</span>MICROLEARNING</li>
      <li>CURRICULUM MAPPING<span class="dot">·</span>XAPI</li>
      <li>ASSESSMENT DESIGN<span class="dot">·</span>LMS</li>
      <li>SIMULATIONS<span class="dot">·</span>VIDEO COURSES</li>
    </ul>
    <p class="closing">LET'S TALK LEARNING.</p>
  </section>
</body>
</html>
```